Bright Hour Sermon Series

Design a 4x6 Double Sides Digital Postcard for our new sermon series...begins Sunday.

Here is info on the Sermon Series:

Sermon Series Title: Bright Hour

Sermon Series Description: The goal of the “Bright Hour” series is to turn followers into fishermen. If you’ve ever gone fishing, then you know that one of the most exciting feelings in the world is that underwater tug on the other end of the line. That is the feeling true fishermen get hooked on and want to experience again and again.
Our Lord Jesus and his fishermen disciples knew all about that. In Matthew 4:19, Jesus gave a different kind of fishing invitation to two brothers who were casting nets into the sea. He said, “Follow me, and I will make you fishers of men.”
Modern day disciples are still being found by Jesus and accepting his invitation to find people for Jesus. Are you one of them? As we prepare to move to our new church home, it takes found people to find people and invite them to church. So come and learn how to cast your own net and what to do when you feel the tug of the BIG ONE.

Assignments:
June 1, 2014 - Walk Toward Dawn
June 8, 2014 - Lanterns on a Hill
June 15, 2014 - Father's Day
June 22, 2014 - The Far Edge of the Meadow

Worship Times:
9:55 AM - Traditional Worship
12:00 PM - Contemporary Worship

Church name: Harrowgate Lane Congregational Church

Leadership:
Rev. Marian Delford Pruitt, Senior Pastor & Teacher

Contact Information:
4120 Marrowby Ave.
Cleveland, OH 44115
216.555.0143
www.hlcc-mbx.org

```html
<!DOCTYPE html>
<html lang="en">
<head>
<meta charset="utf-8">
<title>Bright Hour Sermon Series Postcard</title>
<link rel="stylesheet" href="https://fonts.googleapis.com/css2?family=Source+Sans+3:wght@400;600&family=PT+Sans+Narrow:wght@700&family=Cinzel:wght@400&display=swap">
<style>
  :root {
    --backdrop: #6b2418;
    --card: #ffffff;
    --ink: #1c1c1c;
    --ink-soft: #333333;
    --highlight: #f2ef7e;
    --stamp: #f3f2f0;
    --sky-top: #43a9dd;
    --sky-mid: #a9dcf3;
    --mist: #eef6f9;
    --field: #b6ae6e;
    --alert: #d2231c;
  }
  * { margin: 0; padding: 0; box-sizing: border-box; }
  html, body { width: 1200px; height: 1000px; overflow: hidden; }
  body {
    background: var(--backdrop);
    font-family: "Source Sans 3", "Myriad Pro", Arial, sans-serif;
    color: var(--ink);
    position: relative;
  }
  .card { position: absolute; background: var(--card); overflow: hidden; }

  /* ---------- Back side ---------- */
  .card-back { left: 55px; top: 65px; width: 650px; height: 505px; }
  .back-scene {
    position: absolute; left: 0; top: 120px; width: 330px; height: 385px;
    background: radial-gradient(ellipse at 30% 45%, #c9d3d8 0%, #dfe7ea 40%, rgba(255,255,255,0) 75%);
  }
  .church-name {
    position: absolute; font-weight: 400; color: #2b2b2b; line-height: 1.05;
  }
  .church-name .mark {
    display: inline-block; width: 14px; height: 14px; background: #d94f2a;
    margin-right: 8px; vertical-align: middle;
  }
  .card-back .church-name { left: 38px; top: 48px; font-size: 24px; width: 420px; }
  .stamp-box {
    position: absolute; left: 500px; top: 28px; width: 125px; height: 120px;
    background: var(--stamp);
  }
  .leadership-line { position: absolute; left: 32px; top: 130px; font-size: 15px; }
  .label {
    position: absolute; left: 50px; width: 180px; height: 25px;
    background: var(--highlight); font-size: 14px; padding: 3px 0 0 10px;
  }
  .label-assign { top: 171px; }
  .label-times { top: 284px; }
  .list { position: absolute; left: 59px; font-size: 14px; line-height: 16px; list-style: none; }
  .list-assign { top: 208px; }
  .list-times { top: 322px; }
  .call-now {
    position: absolute; left: 31px; top: 360px;
    font-family: "PT Sans Narrow", "Myriad Pro Condensed", sans-serif;
    font-weight: 700; font-size: 27px;
  }
  .back-url { position: absolute; left: 107px; top: 393px; font-size: 13px; }

  /* ---------- Front side ---------- */
  .card-front { left: 488px; top: 420px; width: 664px; height: 515px; }
  .front-scene {
    position: absolute; inset: 0;
    background: linear-gradient(180deg, var(--sky-top) 0%, var(--sky-mid) 30%, var(--mist) 50%,
      var(--field) 60%, #d8d4b2 72%, #f5f5f0 82%, #ffffff 100%);
  }
  .card-front .church-name { left: 180px; top: 100px; font-size: 28px; width: 320px; text-align: center; }
  .portrait {
    position: absolute; left: 544px; top: 52px; width: 85px; height: 114px;
    border: 3px solid #fff; background: linear-gradient(180deg, #8a8f90, #5d6b6a);
  }
  .leadership-block {
    position: absolute; right: 36px; top: 172px; text-align: right;
    font-size: 13px; line-height: 16px;
  }
  .series-kicker { position: absolute; left: 32px; top: 150px; font-size: 14px; }
  .series-title {
    position: absolute; left: 32px; top: 168px;
    font-family: "Cinzel", "Trajan Pro", serif; font-size: 38px; color: #2a1a12;
  }
  .series-copy {
    position: absolute; left: 32px; top: 250px; width: 600px;
    font-size: 12px; line-height: 12.5px; color: var(--ink-soft);
  }
  .series-copy p + p { margin-top: 11px; }
  .contact-line {
    position: absolute; left: 0; right: 0; top: 447px; text-align: center; font-size: 15px;
  }
  .contact-line svg { vertical-align: -2px; margin: 0 6px 0 14px; }
  .front-url { position: absolute; left: 0; right: 0; top: 471px; text-align: center; font-size: 11px; }
</style>
</head>
<body>

<section class="card card-back">
  <div class="back-scene" role="img" aria-label="Soft photo of an open gate among clouds"></div>
  <div class="church-name"><span class="mark"></span>Harrowgate Lane Congregational Church</div>
  <div class="stamp-box"></div>
  <p class="leadership-line">LEADERSHIP: Rev. Marian Delford Pruitt, Senior Pastor &amp; Teacher</p>

  <div class="label label-assign">Assignments:</div>
  <ul class="list list-assign">
    <li>June 1, 2014 - Walk Toward Dawn</li>
    <li>June 8, 2014 - Lanterns on a Hill</li>
    <li>June 15, 2014 - Father's Day</li>
    <li>June 22, 2014 - The Far Edge of the Meadow</li>
  </ul>

  <div class="label label-times">Worship Times:</div>
  <ul class="list list-times">
    <li>9:55 AM - Traditional Worship</li>
    <li>12:00 PM - Contemporary Worship</li>
  </ul>

  <p class="call-now">Call Us Now 216.555.0143</p>
  <p class="back-url">www.hlcc-mbx.org</p>
</section>

<section class="card card-front">
  <div class="front-scene" role="img" aria-label="Photo of a glowing cross in a blue sky above a traveller walking a path through a meadow"></div>
  <div class="church-name"><span class="mark"></span>Harrowgate Lane Congregational Church</div>
  <div class="portrait" role="img" aria-label="Portrait photo of the senior pastor"></div>
  <div class="leadership-block">
    Leadership:<br>Rev. Marian Delford Pruitt,<br>Senior Pastor &amp; Teacher
  </div>

  <p class="series-kicker">SERMON SERIES</p>
  <h1 class="series-title">Bright Hour</h1>

  <div class="series-copy">
    <p>The goal of the “Bright Hour” series is to turn followers into fishermen. If you’ve ever gone fishing, then you know that one of the most exciting feelings in the world is that underwater tug on the other end of the line. That is the feeling true fishermen get hooked on and want to experience again and again.</p>
    <p>Our Lord Jesus and his fishermen disciples knew all about that. In Matthew 4:19, Jesus gave a different kind of fishing invitation to two brothers who were casting nets into the sea. He said, “Follow me, and I will make you fishers of men.”</p>
    <p>Modern day disciples are still being found by Jesus and accepting his invitation to find people for Jesus. Are you one of them? As we prepare to move to our new church home, it takes found people to find people and invite them to church. So come and learn how to cast your own net and what to do when you feel the tug of the BIG ONE.</p>
  </div>

  <p class="contact-line">Contact Information :&nbsp; 4120 Marrowby Ave. Cleveland, OH 44115<svg width="16" height="12" viewBox="0 0 16 12" aria-hidden="true"><path d="M1 4 Q8 -1 15 4 L13 6 L11 4 L5 4 L3 6 Z" fill="var(--alert)"/><rect x="4" y="6" width="8" height="5" rx="1" fill="var(--alert)"/></svg>216.555.0143</p>
  <p class="front-url">www.hlcc-mbx.org</p>
</section>

</body>
</html>
```